Bag Design For Outdoors Industry

We are a Midwest seed company that is looking for a bag design for our Food Plot Product Line, "Ridgehorn". We are looking for a broad design that will work for several SKUs. Attached is the dieline for 4.5"x9.5"x20.75" bag and specifications for the print company. Also included are the brand standards and our catalog. The bag design should pull the themes and concepts established in the catalog. We will be placing 4"x9" labels on the front and back of the bag (design should have a guide for labels). Front of package will include a clear window to see the product. Use the attached layout PDF for a rough idea of how it should be formatted. The final design should convey the simple brand and overall themes.

Target Market(s)

Outdoor enthusiasts

Industry/Entity Type

Outdoors

Requirements
Must have
• Follow our provided branding, clear window

```html
<!DOCTYPE html>
<html lang="en">
<head>
<meta charset="utf-8">
<title>Ridgehorn Food Plot Seed – Bag Proof</title>
<link rel="stylesheet" href="https://fonts.googleapis.com/css2?family=Arimo:wght@400;700&family=Cinzel:wght@900&family=Montserrat:wght@300;700;800&display=swap">
<style>
  :root{
    --bag-green:#22c703;
    --gusset-light:#7ee07e;
    --panel-black:#070707;
    --seal-gray:#4c5652;
    --window-blue:#63b3fb;
    --dieline-pink:#e040c0;
    --seal-red:#e0504a;
    --ink:#111;
    --alert-red:#e8141b;
    --white:#fff;
  }
  *{margin:0;padding:0;box-sizing:border-box}
  html,body{width:1200px;height:1035px;overflow:hidden;background:var(--white)}
  .proof-sheet{position:relative;width:1200px;height:1035px}
  .dieline-art{position:absolute;left:0;top:0}
  .dim-label{font-family:"Arimo",sans-serif;font-size:6.5px;fill:var(--ink)}
  .wordmark{font-family:"Montserrat",sans-serif;font-weight:800;fill:var(--white)}
  .tagline{font-family:"Montserrat",sans-serif;font-weight:300;fill:var(--white)}
  .slogan{font-family:"Cinzel",serif;font-weight:900;font-size:18.5px;letter-spacing:2px;fill:var(--white)}

  .spec{position:absolute;font-family:"Arimo",sans-serif;font-size:8.6px;line-height:1;color:var(--ink);white-space:nowrap}
  .spec.alert{color:var(--alert-red)}
  .spec.bold{font-weight:700;font-size:10.5px}
  .swatch{position:absolute;width:12px;height:12px;border:1px solid #555}
  .notice-box{position:absolute;left:82px;top:958px;width:457px;height:65px;border:1.2px solid var(--ink);padding:5px 5px;font-family:"Arimo",sans-serif;font-size:7px;line-height:9.6px;color:var(--ink)}
  .notice-box strong{color:var(--alert-red)}
  .checklist{position:absolute;left:731px;top:932px;width:193px;height:91px;border:1.2px solid var(--ink);font-family:"Arimo",sans-serif;font-size:7.4px;color:var(--ink)}
  .checklist h4{position:absolute;left:4px;top:6px;font-size:7.4px;color:var(--alert-red)}
  .checklist ul{list-style:none;position:absolute;right:14px;top:19px;text-align:right}
  .checklist li{height:11.9px;position:relative}
  .checklist li span{color:var(--alert-red)}
  .checklist li::after{content:"";position:absolute;right:-10px;top:0;width:6px;height:6px;border:0.8px solid var(--ink)}
  .approval-box{position:absolute;left:933px;top:959px;width:197px;height:64px;border:1.2px solid var(--ink);font-family:"Arimo",sans-serif;font-size:4.2px;font-weight:700;color:var(--ink);text-align:center}
  .approval-box p{position:absolute;left:0;right:0}
  .approval-row{position:absolute;font-size:4.2px;font-weight:700}
  .approval-row i{display:inline-block;width:6px;height:6px;border:0.8px solid var(--ink);vertical-align:middle;margin:0 3px}
  .sig-line{display:inline-block;width:80px;border-bottom:0.6px solid var(--ink)}
</style>
</head>
<body>
<main class="proof-sheet">

<svg class="dieline-art" width="1200" height="1035" viewBox="0 0 1200 1035" xmlns="http://www.w3.org/2000/svg">
  <!-- dimension rules -->
  <g class="dimensions" stroke="#999" stroke-width="0.5" fill="none">
    <line x1="163" y1="51" x2="1108" y2="51"/>
    <line x1="315" y1="48" x2="315" y2="62"/>
    <line x1="634" y1="48" x2="634" y2="62"/>
    <line x1="785" y1="48" x2="785" y2="62"/>
    <line x1="146" y1="36" x2="146" y2="62"/>
    <line x1="163" y1="36" x2="163" y2="62"/>
    <line x1="1106" y1="36" x2="1106" y2="62"/>
    <line x1="1122" y1="36" x2="1122" y2="62"/>
    <line x1="104" y1="80" x2="121" y2="80"/>
    <line x1="105" y1="80" x2="105" y2="778"/>
    <line x1="634" y1="788" x2="634" y2="800"/>
    <line x1="643" y1="788" x2="643" y2="800"/>
    <line x1="1148" y1="690" x2="1165" y2="690"/>
    <line x1="1148" y1="690" x2="1148" y2="755"/>
  </g>
  <g class="dim-labels">
    <text class="dim-label" x="239" y="47" text-anchor="middle">4.5000 in</text>
    <text class="dim-label" x="474" y="47" text-anchor="middle">9.5000 in</text>
    <text class="dim-label" x="710" y="47" text-anchor="middle">4.5000 in</text>
    <text class="dim-label" x="945" y="48" text-anchor="middle">9.5000 in</text>
    <text class="dim-label" transform="translate(153 58) rotate(-90)">0.3750 in</text>
    <text class="dim-label" transform="translate(162 58) rotate(-90)" style="font-size:4px">0.125 in / 3.175 mm</text>
    <text class="dim-label" transform="translate(1109 58) rotate(-90)">0.125 in / 3.175 mm</text>
    <text class="dim-label" transform="translate(1118 58) rotate(-90)">0.3750 in</text>
    <text class="dim-label" x="108" y="431">20.7500 in</text>
    <text class="dim-label" x="105" y="756" style="font-size:4px">0.394 in /</text>
    <text class="dim-label" x="105" y="762" style="font-size:4px">10 mm</text>
    <text class="dim-label" x="640" y="809" text-anchor="middle">0.289 in / 7.34 mm</text>
    <text class="dim-label" x="1147" y="702" style="font-size:5px">1.995 in /</text>
    <text class="dim-label" x="1147" y="709" style="font-size:5px">50.67mm</text>
    <text class="dim-label" transform="translate(1178 760) rotate(-90)" style="font-size:5.5px">2.620 in / 66.55 mm</text>
  </g>

  <!-- bag panels -->
  <g class="bag-panels">
    <rect x="146" y="80" width="17" height="698" fill="var(--bag-green)"/>
    <rect x="146" y="80" width="12" height="8" fill="var(--panel-black)"/>
    <rect x="146" y="770" width="12" height="8" fill="var(--panel-black)"/>

    <rect class="gusset-left" x="163" y="80" width="148" height="698" fill="var(--bag-green)"/>
    <rect x="163" y="80" width="9" height="698" fill="var(--gusset-light)"/>
    <rect x="306" y="80" width="5" height="698" fill="var(--gusset-light)"/>
    <rect x="311" y="80" width="11" height="698" fill="var(--seal-gray)"/>

    <rect class="panel-front" x="322" y="80" width="305" height="698" fill="var(--panel-black)"/>
    <rect x="627" y="80" width="16" height="698" fill="var(--seal-gray)"/>

    <rect class="gusset-right" x="643" y="80" width="136" height="698" fill="var(--bag-green)"/>
    <rect x="643" y="80" width="7" height="698" fill="var(--gusset-light)"/>
    <rect x="774" y="80" width="5" height="698" fill="var(--gusset-light)"/>
    <rect x="779" y="80" width="15" height="698" fill="var(--seal-gray)"/>

    <rect class="panel-back" x="794" y="80" width="304" height="698" fill="var(--panel-black)"/>
    <rect x="1098" y="80" width="13" height="698" fill="var(--seal-gray)"/>
    <rect x="1111" y="80" width="11" height="698" fill="var(--panel-black)"/>
    <rect x="1111" y="80" width="8" height="8" fill="#000"/>

    <!-- bottom gusset seal band -->
    <rect x="163" y="756" width="959" height="22" fill="var(--seal-gray)"/>
    <rect x="163" y="756" width="220" height="22" fill="var(--gusset-light)"/>
    <rect x="643" y="756" width="90" height="22" fill="var(--gusset-light)"/>
  </g>

  <!-- bottom gusset folds -->
  <g class="gusset-folds" stroke="#fff" stroke-opacity="0.35" stroke-width="10" fill="none">
    <line x1="163" y1="691" x2="232" y2="778"/>
    <line x1="316" y1="694" x2="245" y2="778"/>
    <line x1="316" y1="694" x2="384" y2="778"/>
    <line x1="643" y1="691" x2="712" y2="778"/>
  </g>
  <g class="gusset-triangles" fill="var(--bag-green)">
    <polygon points="94,778 146,709 146,778"/>
    <polygon points="565,778 634,691 703,778"/>
    <polygon points="718,778 782,691 853,778"/>
    <polygon points="1037,778 1104,691 1172,778"/>
  </g>
  <polygon points="787,691 794,691 794,700" fill="var(--bag-green)"/>
  <line x1="794" y1="700" x2="837" y2="756" stroke="#888" stroke-width="2"/>
  <line x1="1098" y1="700" x2="1055" y2="756" stroke="#888" stroke-width="2"/>

  <!-- seal guide ovals -->
  <rect x="164" y="751" width="26" height="13" rx="6" fill="none" stroke="var(--panel-black)" stroke-width="0.6"/>
  <rect x="265" y="751" width="26" height="13" rx="6" fill="none" stroke="var(--panel-black)" stroke-width="0.6"/>

  <!-- gusset wordmarks -->
  <text class="wordmark" font-size="63" letter-spacing="1" transform="translate(206 158) rotate(90)">RIDGEHORN</text>
  <text class="tagline" font-size="14.5" letter-spacing="3" transform="translate(190 469) rotate(90)">FOOD PLOT SEED</text>
  <text class="wordmark" font-size="63" letter-spacing="1" transform="translate(678 158) rotate(90)">RIDGEHORN</text>
  <text class="tagline" font-size="14.5" letter-spacing="3" transform="translate(662 469) rotate(90)">FOOD PLOT SEED</text>

  <!-- front panel -->
  <text class="wordmark" x="475" y="243" font-size="30" text-anchor="middle">RIDGEHORN</text>
  <text class="tagline" x="593" y="252" font-size="7" letter-spacing="2" text-anchor="end">FOOD PLOT SEED</text>
  <rect class="label-guide" x="323.5" y="274.5" width="302" height="134" fill="none" stroke="#ddd" stroke-width="1"/>
  <text class="wordmark" x="475" y="510" font-size="30" text-anchor="middle">RIDGEHORN</text>
  <polygon class="clear-window" points="332,557 609,694 332,694" fill="var(--window-blue)"/>

  <!-- back panel -->
  <text class="slogan" x="940" y="155" text-anchor="middle">SOURCED PURE.</text>
  <text class="slogan" x="940" y="183" text-anchor="middle">PACKAGED FRESH.</text>
  <text class="slogan" x="940" y="211" text-anchor="middle">SIMPLE BRAND.</text>
  <defs>
    <linearGradient id="harvest-tones" x1="0" y1="0" x2="1" y2="0">
      <stop offset="0" stop-color="#3f7a2a"/>
      <stop offset="0.3" stop-color="#a23ccf"/>
      <stop offset="0.6" stop-color="#d8245a"/>
      <stop offset="1" stop-color="#e88a18"/>
    </linearGradient>
    <linearGradient id="wildlife-fade" x1="0" y1="0" x2="0" y2="1">
      <stop offset="0.45" stop-color="#000" stop-opacity="0"/>
      <stop offset="1" stop-color="#5a4a3a" stop-opacity="0.85"/>
    </linearGradient>
  </defs>
  <g role="img" aria-label="Photo collage of forage greens, turnip, clover, corn, a whitetail buck and wild turkeys">
    <rect x="800" y="226" width="299" height="272" fill="url(#harvest-tones)"/>
    <rect x="800" y="226" width="299" height="272" fill="url(#wildlife-fade)"/>
  </g>
  <rect class="label-guide" x="794.5" y="499.5" width="302" height="133" fill="none" stroke="#ddd" stroke-width="1"/>
  <text class="wordmark" x="949" y="690" font-size="30" text-anchor="middle">RIDGEHORN</text>
  <text class="tagline" x="1065" y="698" font-size="7" letter-spacing="2" text-anchor="end">FOOD PLOT SEED</text>

  <!-- dieline & seal guides -->
  <rect x="146" y="80" width="976" height="698" fill="none" stroke="var(--dieline-pink)" stroke-width="0.6"/>
  <g stroke="var(--seal-red)" stroke-width="0.6" stroke-dasharray="4 2">
    <line x1="313" y1="80" x2="313" y2="778"/>
    <line x1="317" y1="80" x2="317" y2="778"/>
    <line x1="636" y1="80" x2="636" y2="778"/>
    <line x1="783" y1="80" x2="783" y2="778"/>
    <line x1="786" y1="80" x2="786" y2="778"/>
  </g>

  <!-- divider -->
  <line x1="82" y1="860" x2="1126" y2="860" stroke="#777" stroke-width="0.8"/>

  <!-- roll direction icon -->
  <g class="unwind-icon" stroke="var(--ink)" stroke-width="0.7" fill="none">
    <rect x="566" y="984" width="26" height="22" rx="3"/>
    <ellipse cx="592" cy="995" rx="3" ry="11"/>
    <line x1="593" y1="982" x2="593" y2="990"/>
  </g>
  <text x="561" y="990" font-family="Arimo, sans-serif" font-size="6" font-weight="700">2</text>

  <!-- legend swatches -->
  <line x1="654" y1="975" x2="671" y2="975" stroke="var(--dieline-pink)" stroke-width="0.8"/>
  <line x1="654" y1="986" x2="671" y2="986" stroke="var(--seal-red)" stroke-width="0.8" stroke-dasharray="4 3"/>
  <rect x="654" y="992" width="17" height="6" fill="#c8f4ff"/>
</svg>

<!-- print specifications -->
<div class="spec" style="left:83px;top:869px">Date: 10.18.21</div>
<div class="spec" style="left:83px;top:898px">Project Name:</div>
<div class="spec" style="left:83px;top:916px">12366 Field Pro</div>
<div class="spec" style="left:83px;top:946px">Template Name: 29.25"W x 21"R</div>

<div class="spec" style="left:210px;top:869px">Material:</div>
<div class="spec" style="left:210px;top:879px">100060 - 30" - .48mil UV PET /</div>
<div class="spec" style="left:210px;top:890px">100042 - 30" - 4.50mil White PE</div>

<div class="spec" style="left:374px;top:869px">Features:</div>
<div class="spec" style="left:374px;top:890px">Tear: No</div>
<div class="spec" style="left:374px;top:910px">Zipper: No</div>
<div class="spec" style="left:374px;top:931px">Hanghole: No</div>

<div class="spec" style="left:469px;top:869px">Measurements:</div>
<div class="spec" style="left:469px;top:890px">Bleed: 0.394”</div>
<div class="spec" style="left:469px;top:900px">Each Side</div>
<div class="spec" style="left:469px;top:921px">Eyemarks</div>
<div class="spec" style="left:469px;top:931px">In Print Area</div>

<div class="spec" style="left:567px;top:869px">Color Specifications:</div>
<span class="swatch" style="left:567px;top:881px;background:#fff"></span><div class="spec" style="left:583px;top:883px">White</div>
<span class="swatch" style="left:567px;top:896px;background:#00e5ff;border:none"></span><div class="spec" style="left:583px;top:898px">Cyan</div>
<span class="swatch" style="left:567px;top:911px;background:#ff00e0;border:none"></span><div class="spec" style="left:583px;top:913px">Magenta</div>
<span class="swatch" style="left:567px;top:925px;background:#fff200;border:none"></span><div class="spec" style="left:583px;top:927px">Yellow</div>
<span class="swatch" style="left:567px;top:940px;background:#000;border:none"></span><div class="spec" style="left:583px;top:942px">Black</div>

<div class="spec" style="left:731px;top:869px">Color Strategy:</div>
<div class="spec" style="left:731px;top:883px">Clear - White</div>
<div class="spec" style="left:731px;top:896px">CMYK</div>
<div class="spec" style="left:731px;top:910px">No white ink</div>

<div class="spec" style="left:962px;top:869px">LUTs:</div>
<div class="spec" style="left:962px;top:883px">XP05</div>

<div class="spec" style="left:1022px;top:869px">Tolerances:</div>
<div class="spec alert" style="left:1022px;top:878px">All Measurements are</div>
<div class="spec alert" style="left:1022px;top:887px">+/- 2mm/0.078in</div>
<div class="spec alert" style="left:1022px;top:902px">Please note: Seal sizes and</div>
<div class="spec alert" style="left:1022px;top:911px">location are approximate</div>

<div class="spec bold" style="left:962px;top:937px">Rev: 1&nbsp; SD-241</div>

<div class="spec" style="left:652px;top:961px">Legend:</div>
<div class="spec" style="left:675px;top:972px">Dieline</div>
<div class="spec" style="left:675px;top:982px">Safe Area</div>
<div class="spec" style="left:675px;top:992px">Seals</div>

<section class="notice-box">
  <strong>PLEASE CHECK CAREFULLY:</strong> Proofs are supplied for proofing of layout, spelling, sizing, features and color breaks.<br>
  Please indicate any corrections needed at once. If no changes are necessary, please sign and return.<br>
  Production will not start until proof is approved and returned. Your approval is our authority to proceed.<br>
  Delay in returning your proof will delay your delivery. We have checked this artwork for accuracy. Final approval is the client’s responsibility.<br>
  Please check for errors before production. Customer assumes all risk for compliance with federal, state and local packaging, advertising and<br>
  labeling laws, regulations and rules. This proof is for layout and copy only and does not reflect final color achievable on press.
</section>

<section class="checklist">
  <h4>CUSTOMER PROOF APPROVAL CHECKLIST:</h4>
  <ul>
    <li><span>SIZE LISTED</span> IS CORRECT:</li>
    <li><span>POUCH FEATURES</span> ARE CORRECT:</li>
    <li><span>SEALS</span> ARE CORRECT:</li>
    <li><span>UPC</span> IS CORRECT:</li>
    <li><span>SPELLING</span> IS CORRECT:</li>
    <li><span>COLORS</span> ARE CORRECT:</li>
  </ul>
</section>

<section class="approval-box">
  <p style="top:5px">YOUR SIGNED APPROVAL IS REQUIRED FOR US TO PROCEED. BY SIGNING,</p>
  <p style="top:13px">YOU ASSUME RESPONSIBILITY FOR THE ACCURACY OF THIS PROOF.</p>
  <div class="approval-row" style="left:34px;top:25px">APPROVED AS IS <i></i> SIGNATURE:<span class="sig-line"></span></div>
  <div class="approval-row" style="left:36px;top:40px">NOT APPROVED <i></i> SIGNATURE:<span class="sig-line"></span></div>
  <p style="top:47px;left:4px;right:auto;width:70px;font-size:3.4px;line-height:4.6px">IF NOT APPROVED, PLEASE SEND DETAILED LIST OF CHANGES TO YOUR SALES SUPPORT SPECIALIST</p>
</section>

</main>
</body>
</html>
```